INCREASED BUDGET -- Cover Art Template Needed For Record Label

We are an electronic music record label that needs a cover art template for our 2017 releases. The design must be easy to update in Photoshop with different text, colors, or patterns.

The winner will also be asked to design our social media banners for Facebook, Twitter, and SoundCloud, so there's an opportunity to make more money.

Words to describe our sound: sophisticated, forward-thinking, futuristic, modern, emotional

Please make the LA logo the focal point of your design. Feel free to modify our logo as needed. Bonus points for anyone that can find a way to visually represent the word "Lanternfold". Examples of artwork that we found attractive are included to provide inspiration.

You can view our previous releases by clicking on any of the links: https://www.tunevaultshop.example/label/lanternfold-audio/52947/releases

Target Market(s)

Electronic music lovers

Industry/Entity Type

Music Download

Font styles to use
Serif
Decorative
Other font styles liked:
• Aller Display, Aller Light

Requirements
Must have
• Lanternfold Audio record logo
• Name of artist: Rufus Delgarde
• Title: Daybreak / Hold Still (Reworks)
Nice to have
• Tracklist:
• Hold Still (Brantlow Remix)
• Daybreak (Zolvarin Remix)
• Catalog number: 318

```html
<!DOCTYPE html>
<html lang="en">
<head>
<meta charset="UTF-8">
<title>Rufus Delgarde – Daybreak / Hold Still (Reworks) – Lanternfold Audio</title>
<link href="https://fonts.googleapis.com/css2?family=Montserrat:wght@300;400;700&display=swap" rel="stylesheet">
<style>
  :root {
    --stage: #eceef1;
    --sleeve: #1a1718;
    --teal: #3fc1c9;
    --ink-light: #e9e9ea;
    --rose: #c4384f;
    --coral: #e8455f;
    --catalog: #cfcfd1;
  }
  * { margin: 0; padding: 0; box-sizing: border-box; }
  html, body {
    width: 1200px;
    height: 864px;
    overflow: hidden;
    background: var(--stage);
    font-family: "Montserrat", Arial, sans-serif;
  }
  .release-cover {
    position: absolute;
    left: 210px;
    top: 42px;
    width: 780px;
    height: 780px;
    background: var(--sleeve);
  }
  .artist-name {
    position: absolute;
    left: 66px;
    top: 52px;
    font-weight: 700;
    font-size: 50px;
    letter-spacing: 1px;
    color: var(--teal);
    text-transform: uppercase;
  }
  .tracklist {
    position: absolute;
    left: 66px;
    top: 118px;
    list-style: none;
    font-weight: 300;
    font-size: 28px;
    line-height: 38px;
    letter-spacing: 1.5px;
    color: var(--ink-light);
    text-transform: uppercase;
  }
  .remix-credit {
    position: absolute;
    left: 66px;
    top: 208px;
    font-weight: 400;
    font-size: 19px;
    letter-spacing: 1px;
    color: var(--rose);
    text-transform: uppercase;
  }
  .label-mark {
    position: absolute;
    right: 70px;
    top: 330px;
    display: flex;
    align-items: center;
    gap: 22px;
  }
  .label-mark__dot {
    width: 34px;
    height: 34px;
    border-radius: 50%;
    background: var(--teal);
  }
  .label-mark__name {
    font-weight: 700;
    font-size: 58px;
    line-height: 66px;
    letter-spacing: 2px;
    color: var(--coral);
    text-transform: uppercase;
    text-align: right;
  }
  .catalog-number {
    position: absolute;
    right: 66px;
    bottom: 50px;
    font-weight: 400;
    font-size: 30px;
    letter-spacing: 1px;
    color: var(--catalog);
  }
</style>
</head>
<body>
  <section class="release-cover" aria-label="Release cover: Rufus Delgarde – Daybreak / Hold Still (Reworks)">
    <h1 class="artist-name">Rufus Delgarde</h1>
    <ol class="tracklist">
      <li>1. Daybreak</li>
      <li>2.Hold Still</li>
    </ol>
    <p class="remix-credit">Brantlow &amp; Zolvarin Remix</p>
    <div class="label-mark">
      <span class="label-mark__dot"></span>
      <span class="label-mark__name">Lanternfold<br>Audio</span>
    </div>
    <p class="catalog-number">LA318</p>
  </section>
</body>
</html>
```